Tab-Fix Notes
3inx3in Tab Fix Notes with "Thank You!" message
Tab-Fix Notes - Corporate Services
Creative Brief
In need of designs for 3inch x 3inch Tab Fix Notes. Company Branding and Image (professional, high energy, uplifting, splash of color) The words "Thank You" and company website (www.marlowbrekke.com) must be included on actual tab fix.
Corporate Services
Corporate and professional, but modern.
3inch by 3 inch tab fix size. Use your creativity to the fullest but handwritten notes must legible on tab-fix. White backgrounds are okay as long as message stands out. Color preference of background - hot pink, orange, neon blue, neon green The words "Thank You" and company website (www.marlowbrekke.com) must be included on actual tab fix.
Related Contests
Social Media Banner Design (for Chatterloop, Zanvio+, Peepwire, and WorkNexa) based on current website.
Concepts
The Beacon Planning Institute Banner Display

```html
<!DOCTYPE html>
<html lang="en">
<head>
<meta charset="utf-8">
<title>Thank You Note</title>
<link rel="stylesheet" href="https://fonts.googleapis.com/css2?family=Montserrat:wght@500;800&display=swap">
<style>
  :root {
    --backdrop: #b9b9b9;
    --paper: #ffffff;
    --blue-light: #2cb4ea;
    --blue-mid: #1592d2;
    --blue-deep: #0a5f9c;
    --blue-flap: #0b4f86;
    --ink-light: #ffffff;
  }
  html, body {
    margin: 0;
    padding: 0;
    width: 1200px;
    height: 901px;
    overflow: hidden;
    background: var(--backdrop);
  }
  .canvas {
    position: relative;
    width: 1200px;
    height: 901px;
  }
  .note {
    position: absolute;
    left: 200px;
    top: 44px;
    width: 805px;
    height: 813px;
    background: var(--paper);
    box-shadow: 0 4px 14px rgba(0,0,0,0.25);
  }
  .band {
    position: absolute;
    left: 0;
    width: 805px;
    height: 100px;
  }
  .band svg {
    position: absolute;
    inset: 0;
    width: 100%;
    height: 100%;
    display: block;
  }
  .band--top { top: 0; }
  .band--bottom { bottom: 0; }
  .band--bottom svg { transform: scaleY(-1); }
  .band__text {
    position: absolute;
    left: 0;
    right: 0;
    text-align: center;
    color: var(--ink-light);
    font-family: "Montserrat", sans-serif;
  }
  .headline {
    top: 6px;
    font-weight: 800;
    font-size: 66px;
    letter-spacing: 7px;
    line-height: 70px;
  }
  .website {
    bottom: 16px;
    font-weight: 500;
    font-size: 40px;
    line-height: 48px;
    letter-spacing: 0.5px;
  }
</style>
</head>
<body>
<div class="canvas">
  <div class="note">
    <div class="band band--top">
      <svg viewBox="0 0 805 100" preserveAspectRatio="none" aria-hidden="true">
        <defs>
          <linearGradient id="bandFillTop" x1="0" x2="1" y1="0" y2="0">
            <stop offset="0" stop-color="var(--blue-deep)"/>
            <stop offset="0.5" stop-color="var(--blue-light)"/>
            <stop offset="1" stop-color="var(--blue-deep)"/>
          </linearGradient>
        </defs>
        <path d="M0 0 H805 V100 C790 88 770 82 740 82 H65 C35 82 15 88 0 100 Z" fill="url(#bandFillTop)"/>
        <path d="M0 0 H40 C25 40 10 70 0 100 Z" fill="var(--blue-flap)"/>
        <path d="M805 0 H765 C780 40 795 70 805 100 Z" fill="var(--blue-flap)"/>
      </svg>
      <div class="band__text headline">Thank You</div>
    </div>
    <div class="band band--bottom">
      <svg viewBox="0 0 805 100" preserveAspectRatio="none" aria-hidden="true">
        <defs>
          <linearGradient id="bandFillBottom" x1="0" x2="1" y1="0" y2="0">
            <stop offset="0" stop-color="var(--blue-deep)"/>
            <stop offset="0.5" stop-color="var(--blue-mid)"/>
            <stop offset="1" stop-color="var(--blue-deep)"/>
          </linearGradient>
        </defs>
        <path d="M0 0 H805 V100 C790 88 770 82 740 82 H65 C35 82 15 88 0 100 Z" fill="url(#bandFillBottom)"/>
        <path d="M0 0 H40 C25 40 10 70 0 100 Z" fill="var(--blue-flap)"/>
        <path d="M805 0 H765 C780 40 795 70 805 100 Z" fill="var(--blue-flap)"/>
      </svg>
      <div class="band__text website">www.marlowbrekke.com</div>
    </div>
  </div>
</div>
</body>
</html>
```